Modern, Clean, Edgy & Fun Comedy Show Flyer

We need to a create a new flyer for the comedy show, Harbor Laugh Nights. The original version of the flyer is attached (file: Old flyer), as well as two versions of the logo.
- The text should be the same except now the show is Every First Wednesday and the next show is June 1.
- Remove the jerk shop logo
- Remove the picture of the man, and replace it with a photo of Dale (our host), the Audience, or something of your own design.
* pictures of Dale and the Audience is attached.
* We'd like to keep the same color palette and have also attached a color palette for reference

I have also attached 4 references of flyers that I like, that you can use to get an idea of the theme and aesthetic we are looking for.
* Files: Reference 1, Reference 2, Reference 3, Reference 4
Updates

Colors
3277b5
85acd3
0455a3
eaf1f7
cee9f5
ecf7fb
d5d5d5
e6e6e6

Requirements
Must have
• The harbor laugh nights logo attached
• The text as specified in the project description
• An option with Dale and without

```html
<!DOCTYPE html>
<html lang="en">
<head>
<meta charset="utf-8">
<title>Harbor Laugh Nights – Comedy Show</title>
<link rel="stylesheet" href="https://fonts.googleapis.com/css2?family=Fira+Sans:wght@600;700;800&display=swap">
<style>
  :root {
    --night-top: #2e3d5e;
    --night-mid: #15244a;
    --night-bottom: #0a1533;
    --brand-blue: #3277b5;
    --ice: #cee9f5;
    --snow: #eaf1f7;
    --mist: #e6e6e6;
    --photo-light: #e4e1e3;
    --photo-dark: #4a3229;
  }
  * { margin: 0; padding: 0; box-sizing: border-box; }
  html, body { width: 1200px; height: 935px; overflow: hidden; background: var(--night-bottom); }
  .flyer {
    position: relative;
    width: 1200px;
    height: 935px;
    overflow: hidden;
    font-family: "Fira Sans", Arial, sans-serif;
    background: linear-gradient(180deg, var(--night-top) 0%, var(--night-mid) 35%, var(--night-bottom) 100%);
    color: var(--snow);
  }
  .show-name {
    position: absolute;
    left: 35px; top: 112px;
    width: 400px;
    text-align: center;
    font-weight: 700;
    font-size: 60px;
    line-height: 1.02;
    color: var(--brand-blue);
  }
  .host {
    position: absolute;
    left: 35px; top: 330px;
    width: 430px;
    text-align: center;
    color: var(--mist);
    font-weight: 700;
  }
  .host-label { font-size: 33px; line-height: 1.1; }
  .host-name { font-size: 58px; line-height: 1.2; margin-top: 2px; }
  .host-photo {
    position: absolute;
    left: 88px; top: 471px;
    width: 324px; height: 382px;
    background: linear-gradient(135deg, var(--photo-light) 0%, #8a6a5c 45%, var(--photo-dark) 70%, #b9b2b3 100%);
  }
  .headline {
    position: absolute;
    left: 530px; top: 121px;
    font-weight: 800;
    font-size: 88px;
    line-height: 1;
    color: var(--snow);
    letter-spacing: 1px;
  }
  .schedule {
    position: absolute;
    left: 532px; top: 222px;
    font-weight: 800;
    font-size: 61px;
    line-height: 1;
    color: var(--snow);
  }
  .schedule sup { font-size: 33px; vertical-align: 23px; }
  .featuring {
    position: absolute;
    left: 555px; top: 304px;
    font-size: 35px; font-weight: 700;
    color: var(--brand-blue);
  }
  .lineup { position: absolute; left: 532px; top: 366px; width: 660px; }
  .comic { position: absolute; font-size: 41px; font-weight: 700; white-space: nowrap; }
  .comic.ice { color: var(--ice); }
  .comic.mist { color: var(--mist); }
  .event-date {
    position: absolute;
    left: 515px; top: 580px; width: 600px;
    text-align: center;
    font-size: 58px; font-weight: 800; color: var(--snow);
  }
  .venue {
    position: absolute;
    left: 530px; top: 677px; width: 545px;
    text-align: center;
    color: var(--ice);
    font-weight: 700;
  }
  .venue-name { font-size: 47px; line-height: 1; }
  .venue-address { font-size: 40px; line-height: 1; margin-top: 12px; }
  .admission {
    position: absolute;
    left: 529px; top: 818px;
    display: flex; align-items: center; gap: 26px;
    font-size: 47px; font-weight: 800; color: var(--snow);
  }
  .admission .divider { width: 2px; height: 40px; background: var(--snow); }
</style>
</head>
<body>
<div class="flyer">
  <div class="show-name">Harbor Laugh Nights</div>

  <div class="host">
    <div class="host-label">Hosted by</div>
    <div class="host-name">Dale Morrow</div>
  </div>

  <div class="host-photo" role="img" aria-label="Photo of host Dale Morrow performing on stage with a microphone"></div>

  <h1 class="headline">COMEDY SHOW</h1>
  <div class="schedule">EVERY 1<sup>st</sup> WEDNESDAY</div>

  <div class="featuring">featuring...</div>
  <div class="lineup">
    <span class="comic ice" style="left:0; top:0;">Wendell Carver</span>
    <span class="comic ice" style="left:342px; top:0;">Sam Loweth</span>
    <span class="comic mist" style="left:0; top:60px;">Reid Halverstone</span>
    <span class="comic ice" style="left:365px; top:60px;">Arun Desmond</span>
    <span class="comic ice" style="left:0; top:112px;">Tess Okafor</span>
  </div>

  <div class="event-date">WEDNESDAY, JUN. 1</div>

  <div class="venue">
    <div class="venue-name">The Tin Lantern</div>
    <div class="venue-address">48 Ferris Avenue, Brooklyn</div>
  </div>

  <div class="admission">
    <span>Adm: FREE</span>
    <span class="divider"></span>
    <span>Doors 6:30 PM</span>
  </div>
</div>
</body>
</html>
```